Baby Boutique Needs a Business Card Design

We need a modern double sided business card design using the attached logo for Lil' Tot Nook.

Lil' Tot Nook is a baby boutique which sells only handmade clothing and accessories for both boys and girls. Our store will live exclusively online.

We would like to only use the colors that have been used in the logo.

Target Market(s)

Potential wholesale clients, Small business owners

Industry/Entity Type

Retail

Contact Information for Business Card

Name Wendell J. Ferris (Owner)
Email sales@ltotnook.com
Main Phone 787-203-6159
Cell phone 787-203-6742
Website www.LTotNook.com

Font styles to use
Sans Serif

Colors

Designer to choose colors to be used in the design.

Requirements
Must have
• -Would like to have icons that indentify the contact information.
• -Include our website
• -Include our tagline in a small area near the bottom. "Handmade Baby Creations"
• -Would like to include Facebook and Instagram Icons
• -
Nice to have
• Would like to have a simple back side with the logo.
• Something along the lines of the harbor ledger card attached.

```html
<!DOCTYPE html>
<html lang="en">
<head>
<meta charset="utf-8">
<title>Lil' Tot Nook — Business Card</title>
<link rel="stylesheet" href="https://fonts.googleapis.com/css2?family=Josefin+Sans:wght@300;400&display=swap">
<style>
  :root {
    --backdrop: #e7e7e6;
    --card: #ffffff;
    --teal: #74c8b8;
    --coral: #df5c5c;
    --ink: #3a3a3a;
    --shadow: rgba(0, 0, 0, 0.14);
  }
  * { box-sizing: border-box; margin: 0; padding: 0; }
  html, body { width: 1200px; height: 850px; overflow: hidden; }
  body {
    background: var(--backdrop);
    font-family: "Josefin Sans", sans-serif;
    color: var(--ink);
    position: relative;
  }
  .card {
    position: absolute;
    width: 620px;
    height: 354px;
    background: var(--card);
    border-radius: 22px;
    overflow: hidden;
    box-shadow: 0 14px 30px var(--shadow);
  }
  .card--back { left: 500px; top: 66px; }
  .card--front { left: 90px; top: 430px; }

  .brand {
    display: flex;
    align-items: center;
    gap: 10px;
    color: var(--teal);
    font-weight: 400;
    letter-spacing: 0.01em;
    white-space: nowrap;
  }
  .brand__dot {
    width: 14px; height: 14px;
    border-radius: 50%;
    background: var(--coral);
    flex: none;
  }
  .card--back .brand {
    position: absolute;
    left: 50%; top: 50%;
    transform: translate(-50%, -50%);
    font-size: 46px;
  }
  .card--front .brand {
    position: absolute;
    right: 44px; top: 62px;
    font-size: 34px;
  }

  .holder {
    position: absolute;
    left: 44px; top: 100px;
    width: 250px;
  }
  .holder__name {
    color: var(--coral);
    font-weight: 300;
    font-size: 27px;
    letter-spacing: 0.02em;
    padding-bottom: 6px;
    border-bottom: 1.5px solid var(--teal);
    white-space: nowrap;
  }
  .holder__role {
    font-size: 13px;
    font-weight: 300;
    margin-top: 3px;
  }

  .contacts {
    position: absolute;
    left: 44px; top: 172px;
    list-style: none;
    display: grid;
    gap: 6px;
  }
  .contacts li {
    display: flex;
    align-items: center;
    gap: 10px;
    font-size: 15px;
    font-weight: 300;
    line-height: 17px;
  }
  .contacts__icon {
    width: 17px; height: 17px;
    border-radius: 50%;
    background: var(--teal);
    color: #fff;
    font-size: 9px;
    font-weight: 400;
    display: grid;
    place-items: center;
    line-height: 1;
    padding-top: 2px;
    flex: none;
  }

  .social {
    position: absolute;
    right: 44px; top: 236px;
    display: flex;
    gap: 10px;
    list-style: none;
  }
  .social__badge {
    width: 26px; height: 26px;
    border-radius: 50%;
    background: var(--teal);
  }

  .tagline-band {
    position: absolute;
    left: 0; right: 0; bottom: 0;
    height: 66px;
    background: var(--coral);
    border-top: 4px solid var(--teal);
    display: flex;
    align-items: center;
    justify-content: center;
  }
  .tagline-band__text {
    color: #fff;
    font-weight: 300;
    font-size: 21px;
    letter-spacing: 0.16em;
    text-transform: uppercase;
    padding-top: 4px;
  }
</style>
</head>
<body>

  <section class="card card--back" aria-label="Card back">
    <div class="brand"><span class="brand__dot"></span>Lil' Tot Nook</div>
  </section>

  <section class="card card--front" aria-label="Card front">
    <div class="brand"><span class="brand__dot"></span>Lil' Tot Nook</div>

    <div class="holder">
      <p class="holder__name">Wendell J. Ferris</p>
      <p class="holder__role">owner</p>
    </div>

    <ul class="contacts">
      <li><span class="contacts__icon">T</span>787-203-6159</li>
      <li><span class="contacts__icon">C</span>787-203-6742</li>
      <li><span class="contacts__icon">E</span>sales@ltotnook.com</li>
      <li><span class="contacts__icon">W</span>www.LTotNook.com</li>
    </ul>

    <ul class="social" aria-label="Social profiles">
      <li class="social__badge" role="img" aria-label="Social profile badge"></li>
      <li class="social__badge" role="img" aria-label="Social profile badge"></li>
    </ul>

    <div class="tagline-band">
      <p class="tagline-band__text">Handmade Baby Creations</p>
    </div>
  </section>

</body>
</html>
```